Name card design for KOV mobile accessories company

KOV is an upmarket brand, we are looking for professional business card design.

the design should be neat and simple but giving a strong feeling.
should not be colorful. make it black/white/gray tone

Name:
Job title:
Contact no.:
company address: i would like the company address to be very small and thin.
link to social media profile:
company website:

*the company have no website yet
as the project is done please i also would like the font that use in design as well; for more further people in company need a business card:)
Updates

Thank you for all super fast submission :D they're all look cool!

i have just update my brief to make the statement clearer, please check it out :)
if you have any question please dont hesitate to ask.
i would like see more design from you! 
Keep it up!  :D

Target Market(s)

Company target are upmarket company distributor, such as Vordane and Pilto store.

Industry/Entity Type

Business

Font styles to use
Serif
Sans Serif
Other font styles liked:
• Formal and mordern

Colors
ffffff
eeeeee
d3d3d3
919191
474747
1b1b1b
000000
333333

Requirements
Must have
• The design must be professional clean and clear but also Strong and Modern!
text should be formal and mordern
Should not have
• No complicated design!

```html
<!DOCTYPE html>
<html lang="en">
<head>
<meta charset="utf-8">
<title>KOV Business Card</title>
<link rel="stylesheet" href="https://fonts.googleapis.com/css2?family=Open+Sans:wght@300;400&display=swap">
<style>
  :root {
    --backdrop: #eeeeee;
    --card-dark: #333333;
    --card-light: #d3d3d3;
    --ink-dark: #474747;
    --ink-soft: #919191;
    --ink-light: #eeeeee;
    --logo-faint: #e4e4e4;
  }
  * { margin: 0; padding: 0; box-sizing: border-box; }
  html, body {
    width: 1200px; height: 900px; overflow: hidden;
    background: var(--backdrop);
    font-family: "Open Sans", sans-serif;
    font-weight: 300;
  }
  .sheet {
    width: 1200px; height: 900px;
    display: flex; flex-direction: column;
    align-items: center; justify-content: center;
    gap: 60px;
  }
  .card {
    width: 560px; height: 320px;
    position: relative;
    box-shadow: 0 4px 14px rgba(0,0,0,0.18);
  }
  .card--front {
    background: var(--card-dark);
    display: flex; flex-direction: column;
    align-items: center; justify-content: center;
  }
  .brand-name {
    font-weight: 300;
    letter-spacing: 10px;
    line-height: 1;
  }
  .card--front .brand-name {
    font-size: 96px;
    color: var(--ink-light);
  }
  .card--front .website {
    margin-top: 26px;
    font-size: 15px;
    letter-spacing: 2px;
    color: var(--ink-soft);
  }
  .card--back {
    background: var(--card-light);
    color: var(--ink-dark);
  }
  .card--back .brand-name {
    position: absolute; left: 34px; top: 28px;
    font-size: 70px;
    color: var(--logo-faint);
  }
  .identity {
    position: absolute; left: 150px; top: 122px;
  }
  .person-name { font-size: 19px; font-weight: 400; letter-spacing: 1px; }
  .job-title { font-size: 15px; margin-top: 2px; }
  .contacts {
    position: absolute; left: 150px; top: 196px;
    list-style: none; font-size: 14px; line-height: 30px;
  }
  .contacts .label { margin-right: 6px; }
  .social-mark {
    display: inline-block; width: 12px; height: 12px;
    background: var(--ink-dark); margin-right: 8px;
    vertical-align: -1px;
  }
  .address {
    position: absolute; right: 30px; bottom: 26px;
    text-align: right; font-size: 13px; font-weight: 300;
    line-height: 18px; color: var(--ink-dark);
    font-style: normal;
  }
</style>
</head>
<body>
  <main class="sheet">
    <section class="card card--front">
      <div class="brand-name">KOV</div>
      <div class="website">www.kov-mobile.com</div>
    </section>
    <section class="card card--back">
      <div class="brand-name">KOV</div>
      <div class="identity">
        <div class="person-name">DARIEN MOLT</div>
        <div class="job-title">Founder &amp; CEO</div>
      </div>
      <ul class="contacts">
        <li><span class="label">M</span>555-014-2290</li>
        <li>www.kov-mobile.com</li>
        <li><span class="social-mark"></span>/kov-mobile</li>
      </ul>
      <address class="address">1420 Harbor Plaza, Suite 310,<br>Brookvale, MI 48210</address>
    </section>
  </main>
</body>
</html>
```